Update shopping site

Our current shopping website is outdated and we are wanting to update our shopping site to have a fresh new look/design.

Create a Web Design (Uncoded - PSD layout only)

We want you to develop the design for 4 pages:
1) Home Page
2) Remedy Type
3) Health Condition
4) Consultations

www.fernlowmeadow.com

Reason: Close to choosing design and a few missing items to be resolved.

Industry/Entity Type

Shopping

```html
<!DOCTYPE html>
<html lang="en">
<head>
<meta charset="utf-8">
<title>Remedy Type – Fernlow Meadow</title>
<link rel="stylesheet" href="https://fonts.googleapis.com/css2?family=Merriweather:wght@400;700&family=Open+Sans:wght@400;600;700&display=swap">
<style>
:root{
  --green:#4f7d12;
  --ink:#2b2b2b;
  --line:#e2e0da;
  --beige:#eeebe1;
  --cream:#f5f3ee;
  --footer-bar:#ebe7dc;
  --star:#f4b41a;
}
*{box-sizing:border-box;margin:0;padding:0}
html,body{width:1200px;height:2305px;overflow:hidden}
body{position:relative;background:#fff;font-family:"Open Sans",Arial,sans-serif;color:var(--ink)}
a{color:inherit;text-decoration:none}
.abs{position:absolute}

/* header */
.topbar{position:absolute;left:0;top:0;width:1200px;height:74px;background:#faf9f6}
.brand{position:absolute;left:161px;top:18px;height:40px;display:flex;align-items:center;gap:10px}
.brand-mark{width:38px;height:38px;border-radius:50%;border:2px solid var(--green)}
.brand-name{font-family:"Merriweather",Georgia,serif;font-size:20px;color:var(--green);font-weight:400}
.account-links{position:absolute;left:611px;top:28px;font-size:12px;font-weight:600;color:#555;display:flex;gap:18px}
.signin{position:absolute;left:790px;top:25px;width:70px;height:26px;border-radius:13px;background:var(--green);color:#fff;font-size:11px;font-weight:700;display:flex;align-items:center;justify-content:center}
.search{position:absolute;left:882px;top:25px;width:156px;height:25px;border:1px solid #d8d6d0;border-radius:13px;background:#fff;font-size:10px;color:#aaa;padding:6px 12px}
.search svg{position:absolute;right:10px;top:6px}

.mainnav{position:absolute;left:0;top:74px;width:1200px;height:55px;background:var(--beige)}
.findus{position:absolute;left:161px;top:0;width:132px;height:55px;background:var(--green);color:#fff;font-size:12px;font-weight:700;display:flex;align-items:center;justify-content:center;gap:10px}
.navlist{position:absolute;top:0;height:55px;list-style:none;font-size:12px;font-weight:600;color:#666}
.navlist li{position:absolute;top:20px;white-space:nowrap}
.navlist li.active{color:var(--green)}
.navlist li.active::after{content:"";position:absolute;left:-12px;right:-12px;top:33px;height:2px;background:var(--green)}
.caret{font-size:9px}

/* hero */
.hero{position:absolute;left:0;top:129px;width:1200px;height:524px;background:radial-gradient(ellipse at 45% 40%,#6b5a34 0%,#2a2a22 40%,#141614 75%,#0d0f0e 100%)}
.hero-title{position:absolute;left:161px;top:310px;font-family:"Merriweather",Georgia,serif;font-weight:700;font-size:42px;color:#fff}
.hero-text{position:absolute;left:161px;top:378px;width:460px;font-size:12px;line-height:23px;color:#f1f1f1;white-space:nowrap}

/* catalogue */
.sidebar-title{position:absolute;left:161px;top:802px;font-family:"Merriweather",Georgia,serif;font-weight:700;font-size:18px;color:var(--green)}
.categories{position:absolute;left:161px;top:848px;list-style:none;font-size:12px;font-weight:600;color:#333}
.categories li{height:30px;padding-left:12px;position:relative}
.categories li::before{content:"›";position:absolute;left:0;top:-1px;font-size:13px}

.toolbar{position:absolute;left:419px;top:760px;width:619px;height:20px;font-size:11px;font-weight:700;color:#222}
.toolbar .count span{color:var(--green)}
.toolbar > div{position:absolute;top:0;white-space:nowrap}

.card{position:absolute;width:170px;height:257px;border:1px solid var(--line);border-bottom:3px solid var(--green);background:#fff;text-align:center}
.card.is-selected{border:2px solid var(--green)}
.card-media{position:absolute;left:26px;top:4px;width:118px;height:166px;background:linear-gradient(180deg,#f7f4f0 0%,#e9e3dc 100%)}
.card-media.photo{left:0;top:28px;width:168px;height:112px}
.card-name{position:absolute;left:0;right:0;top:184px;font-family:"Merriweather",Georgia,serif;font-weight:700;font-size:12.5px;color:#222}
.card.is-selected .card-name{color:var(--green)}
.card-meta{position:absolute;left:10px;right:10px;top:206px;font-size:11px;line-height:15px;color:#333}
.badge{position:absolute}

.pager{position:absolute;left:419px;top:1752px;height:27px;display:flex;font-size:10px;color:#bbb}
.pager span{width:30px;height:27px;display:flex;align-items:center;justify-content:center;border-bottom:2px solid #e4e2dc}
.pager span.current{color:#333;border-bottom-color:var(--green)}
.pager .next{width:61px;background:var(--green);color:#fff;font-weight:700;border-bottom:none}

/* footer */
.footer{position:absolute;left:0;top:1889px;width:1200px;height:378px;background:var(--cream);border-top:2px solid #ddd9cf}
.footer .brand{top:85px}
.mission{position:absolute;left:161px;top:158px;width:340px;font-size:10.5px;line-height:19px;color:#333;white-space:nowrap}
.contact{position:absolute;left:161px;top:218px;font-size:10.5px;line-height:19px;color:#333}
.contact b{font-weight:600}
.contact a{color:var(--green)}
.fcol{position:absolute;font-size:11px;color:#333}
.fcol h4{font-size:11px;font-weight:700;text-transform:uppercase;margin-bottom:8px;color:#222}
.fcol ul{list-style:none;line-height:22.4px}
.totop{position:absolute;left:1120px;top:2196px;width:26px;height:25px;background:#ebe7dc;display:flex;align-items:center;justify-content:center}
.bottombar{position:absolute;left:0;top:2267px;width:1200px;height:38px;background:var(--footer-bar);font-size:10px;font-weight:600;color:#777}
.bottombar .copy{position:absolute;left:161px;top:12px}
.bottombar .legal{position:absolute;right:162px;top:12px}
</style>
</head>
<body>

<header class="topbar">
  <a class="brand" href="#"><span class="brand-mark"></span><span class="brand-name">Fernlow Meadow</span></a>
  <nav class="account-links"><a href="#">My account</a><a href="#">Shopping cart</a></nav>
  <a class="signin" href="#">Sign in</a>
  <div class="search">Search...
    <svg width="11" height="11" viewBox="0 0 12 12"><circle cx="5" cy="5" r="3.8" fill="none" stroke="#aaa" stroke-width="1.4"/><line x1="8" y1="8" x2="11" y2="11" stroke="#aaa" stroke-width="1.4"/></svg>
  </div>
</header>

<nav class="mainnav">
  <a class="findus" href="#">Find us
    <svg width="12" height="16" viewBox="0 0 12 16"><path d="M6 1a5 5 0 0 0-5 5c0 4 5 9 5 9s5-5 5-9a5 5 0 0 0-5-5z" fill="none" stroke="#fff" stroke-width="1.4"/><circle cx="6" cy="6" r="1.8" fill="none" stroke="#fff" stroke-width="1.3"/></svg>
  </a>
  <ul class="navlist">
    <li style="left:410px">Home</li>
    <li class="active" style="left:473px">Remedy Type <span class="caret">⌄</span></li>
    <li style="left:576px">Health Condition <span class="caret">⌄</span></li>
    <li style="left:700px">Accessories &amp; Supplies <span class="caret">⌄</span></li>
    <li style="left:856px">Loyalty Program</li>
    <li style="left:978px">Contact us</li>
  </ul>
</nav>

<section class="hero" role="img" aria-label="Dark still life of a honey pot, lemon slice, ginger root and a tea mug"></section>
<h1 class="hero-title">Remedy Type</h1>
<p class="hero-text">We have the best doctors, Herbalist, Aromatherapist and Health Professional<br>that are ready to offers consultation and helping others with their vast insights<br>In their fields..</p>

<h2 class="sidebar-title">Products Categories</h2>
<ul class="categories">
  <li>Creams &amp; Salves</li>
  <li>Tinctures &amp; Glycerites</li>
  <li>Dried Herbs &amp; Teas</li>
  <li>Aromatherapy</li>
  <li>Oils &amp; Butters</li>
  <li>Bath &amp; Beauty</li>
  <li>Spices</li>
</ul>

<div class="toolbar">
  <div class="count" style="left:0"><span>492</span> PRODUCTS FOUND</div>
  <div style="left:203px">SORT BY: &nbsp;DEFAULT &nbsp;⌄</div>
  <div style="left:395px">SHOW: &nbsp;9 &nbsp;⌄</div>
  <div style="left:526px">VIEW</div>
  <svg class="abs" style="left:569px;top:1px" width="16" height="16" viewBox="0 0 16 16" fill="#4f7d12"><rect x="0" y="0" width="4" height="4"/><rect x="6" y="0" width="4" height="4"/><rect x="12" y="0" width="4" height="4"/><rect x="0" y="6" width="4" height="4"/><rect x="6" y="6" width="4" height="4"/><rect x="12" y="6" width="4" height="4"/><rect x="0" y="12" width="4" height="4"/><rect x="6" y="12" width="4" height="4"/><rect x="12" y="12" width="4" height="4"/></svg>
  <svg class="abs" style="left:599px;top:2px" width="20" height="14" viewBox="0 0 20 14" fill="#ccc"><rect x="0" y="0" width="3" height="2"/><rect x="5" y="0" width="15" height="2"/><rect x="0" y="6" width="3" height="2"/><rect x="5" y="6" width="15" height="2"/><rect x="0" y="12" width="3" height="2"/><rect x="5" y="12" width="15" height="2"/></svg>
</div>

<!-- row 1 -->
<article class="card is-selected" style="left:419px;top:806px">
  <div class="card-media" role="img" aria-label="Amber dropper bottle of herbal tincture"></div>
  <h3 class="card-name">Agrimony</h3>
  <p class="card-meta">Extract (Tincture)<br>(Agrimonia Eupatoria)</p>
</article>
<article class="card" style="left:642px;top:806px">
  <div class="card-media photo" role="img" aria-label="White bowl of essential oil with a blue flower" style="background:linear-gradient(180deg,#7a6a50 0%,#a89a7a 45%,#d9d2c0 100%)"></div>
  <h3 class="card-name">Lavender (French)</h3>
  <p class="card-meta">Essential Oil (Lavandula<br>angustifolia)</p>
</article>
<article class="card" style="left:866px;top:806px">
  <div class="card-media" role="img" aria-label="Amber dropper bottle of herbal tincture"></div>
  <h3 class="card-name">Damiana</h3>
  <p class="card-meta">Extract (Tincture)<br>(Turnera diffusa)</p>
</article>

<!-- row 2 -->
<article class="card" style="left:419px;top:1118px">
  <div class="card-media" role="img" aria-label="Amber dropper bottle of herbal tincture"></div>
  <h3 class="card-name">Chasteberry / Vitex</h3>
  <p class="card-meta">Extract (Tincture) (Vitex<br>agnus-castus )</p>
</article>
<svg class="badge" style="left:573px;top:1104px" width="30" height="30" viewBox="0 0 30 30"><polygon points="15,1 19,10 29,11 21.5,18 24,28 15,23 6,28 8.5,18 1,11 11,10" fill="#f4b41a"/><text x="15" y="20" text-anchor="middle" font-family="Open Sans,Arial,sans-serif" font-size="10" font-weight="700" fill="#fff">5</text></svg>
<article class="card" style="left:642px;top:1118px">
  <div class="card-media photo" role="img" aria-label="Cup of loose herbal tea blend with dried flowers" style="background:linear-gradient(180deg,#e7e3df 0%,#8a6a55 55%,#cfc6bd 100%)"></div>
  <h3 class="card-name">After Dinner</h3>
</article>
<article class="card" style="left:866px;top:1118px">
  <div class="card-media photo" role="img" aria-label="Woven basket of dried herb bundles" style="background:linear-gradient(180deg,#d8d2c6 0%,#9c8156 50%,#5a4530 100%)"></div>
  <h3 class="card-name">Seasonal Ease</h3>
</article>

<!-- row 3 -->
<article class="card" style="left:419px;top:1442px">
  <div class="card-media" role="img" aria-label="Amber dropper bottle of herbal formulation"></div>
  <h3 class="card-name">Alterative</h3>
  <p class="card-meta">Formulation (Extract)</p>
</article>
<article class="card" style="left:642px;top:1442px">
  <div class="card-media" role="img" aria-label="Amber dropper bottle of herbal formulation"></div>
  <h3 class="card-name">Anti-Diarrhoea</h3>
  <p class="card-meta">Formulation<br>(Extract)</p>
</article>
<article class="card" style="left:866px;top:1442px">
  <div class="card-media" role="img" aria-label="Amber dropper bottle of herbal tincture"></div>
  <h3 class="card-name">Angelica</h3>
  <p class="card-meta">Extract (Tincture)<br>(Angelica Archangelica)</p>
</article>

<nav class="pager">
  <span class="current">1</span><span>2</span><span>3</span><span>4</span><span>5</span><span>6</span><span>7</span><span class="next">NEXT</span>
</nav>

<footer class="footer">
  <a class="brand" href="#"><span class="brand-mark"></span><span class="brand-name">Fernlow Meadow</span></a>
  <p class="mission">Fernlow Meadow's mission is to provide our clients with exceptional plant<br>based Health Care products to purify and uplift the body and spirit.</p>
  <p class="contact"><b>Tel:</b> <a href="#">604.555.0148</a><br><b>Fax:</b> <a href="#">604.555.0149</a><br><b>Email:</b> <a href="#">info@fernlowmeadow.com</a></p>

  <div class="fcol" style="left:536px;top:95px">
    <h4>Main Links</h4>
    <ul><li>Home</li><li>Remedy Type</li><li>Health Conditions</li><li>Loyalty Program</li><li>About Us</li><li>Contact us</li></ul>
  </div>
  <div class="fcol" style="left:723px;top:95px">
    <h4>Information</h4>
    <ul><li>Shipping Information</li><li>Consultation</li><li>Community Links</li><li>Health Info</li><li>Returns Policy</li><li>Returns</li></ul>
  </div>
  <div class="fcol" style="left:911px;top:95px">
    <h4>My Account</h4>
    <ul><li>My Account</li><li>Order History</li><li>Newsletter</li></ul>
  </div>
  <div class="fcol" style="left:911px;top:212px">
    <h4>Extras</h4>
    <ul><li>Brands</li><li>Gift Vouchers</li><li>Specials</li></ul>
  </div>
</footer>
<a class="totop" href="#" aria-label="Back to top"><svg width="10" height="6" viewBox="0 0 10 6"><polyline points="1,5 5,1 9,5" fill="none" stroke="#777" stroke-width="1.4"/></svg></a>

<div class="bottombar">
  <span class="copy">Fernlow Meadow Herbal Dispensary © 2017</span>
  <span class="legal">Privacy Policy - Terms &amp; Conditions - Site Map</span>
</div>

</body>
</html>
```